Chirper Bootstrap Website Design (Gaming Themed)

I need a website designed using Chirper Bootstrap for a Rewards website. We'd like to see a gaming based design as the site will cater mostly to gamers.
This is a rewards site similar to sites like LootPenny
I only need the HTML/CSS design.
I need these pages:
1. Homepage for non-logged in users which will also have a sign up form
2. Homepage for logged in users
3. Profile Page
4. Rewards page which will display items that the user can redeem
a) A drop-down to sort by item category
5. Rewards page item details which will display a single item's details
6. About, FAQ, Terms Of Service Pages
Target Market(s)
13 to 30 year old gamers
Mostly males
Industry/Entity Type
It Service
Look and feel

```html
<!DOCTYPE html>
<html lang="en">
<head>
<meta charset="utf-8">
<title>LootPenny – Earn money playing games</title>
<link href="https://fonts.googleapis.com/css2?family=Montserrat:wght@400;600;700&family=Open+Sans:wght@400;600;700&display=swap" rel="stylesheet">
<style>
:root{
  --teal-dark:#0f3b3c;
  --teal:#1c5a57;
  --teal-mid:#2a6f6a;
  --orange:#f7941d;
  --orange-light:#ffb43a;
  --orange-band:#f98a12;
  --purple:#3a2f78;
  --purple-light:#5646a0;
  --grey-bg:#efefef;
  --grey-text:#8c8c8c;
  --white:#ffffff;
  --blue:#1d65b3;
  --blue-dark:#12498a;
}
*{box-sizing:border-box;margin:0;padding:0}
html,body{width:1200px;height:2597px;overflow:hidden}
body{position:relative;font-family:"Open Sans",Arial,sans-serif;background:var(--white);color:#555}
.abs{position:absolute}

/* header */
.site-header{left:0;top:0;width:1200px;height:73px;background:linear-gradient(#1e5253,var(--teal-dark))}
.logo{left:112px;top:20px;font-family:"Montserrat",sans-serif;font-weight:700;font-size:26px;color:#2f6466;letter-spacing:1px}
.btn-signup{left:815px;top:18px;width:167px;height:37px;background:linear-gradient(var(--orange-light),var(--orange));border-radius:3px;color:#fff;font-size:15px;font-weight:600;text-align:center;line-height:37px}
.btn-login{left:1013px;top:18px;width:73px;height:37px;background:linear-gradient(#2c6564,#1a4647);border:1px solid #3c7574;border-radius:3px;color:#d9ecea;font-size:15px;text-align:center;line-height:35px}

/* hero */
.hero-photo{left:0;top:73px;width:1200px;height:519px;background:linear-gradient(90deg,#cfd3d0 0%,#e6e8e4 30%,#dcdfdb 60%,#eeeeea 100%)}
.hero-device{left:165px;top:120px;width:430px;height:472px;background:linear-gradient(160deg,#3a3a3a,#1b1b1b 40%,#d9b59b 80%);border-radius:20px;opacity:.85}
.hero-title{left:717px;top:110px;width:430px;font-family:"Montserrat",sans-serif;font-weight:700;font-size:31px;line-height:40px;color:var(--teal)}
.signup-card{left:717px;top:208px;width:369px;height:324px;background:#fff;box-shadow:0 2px 8px rgba(0,0,0,.15)}
.signup-card h2{position:absolute;left:0;top:14px;width:100%;text-align:center;font-size:15px;font-weight:700;color:var(--teal)}
.btn-social{position:absolute;left:23px;top:44px;width:320px;height:52px;background:linear-gradient(#2b7dd0,var(--blue-dark));border-radius:3px;color:#fff;font-family:"Montserrat",sans-serif;font-weight:600;font-size:21px;text-align:center;line-height:52px}
.signup-note{position:absolute;left:0;top:104px;width:100%;text-align:center;font-size:10px;color:#888}
.field{position:absolute;left:26px;width:312px;height:28px;border:1px solid #d8d8d8;background:#fafafa}
.field .ico{position:absolute;left:0;top:0;width:30px;height:26px;border-right:1px solid #ddd;display:flex;align-items:center;justify-content:center}
.field span.ph{position:absolute;left:42px;top:5px;font-size:12px;color:#999}
.btn-start{position:absolute;left:213px;top:275px;width:132px;height:37px;background:linear-gradient(var(--orange-light),var(--orange));border-radius:3px;color:#fff;font-size:15px;font-weight:700;text-align:center;line-height:37px}

/* features */
.features{left:0;top:592px;width:1200px;height:400px;background:#fff}
.feature{width:360px;text-align:center}
.feature .orb{margin:0 auto;width:192px;height:192px;border-radius:50%;background:linear-gradient(#f2f2f2,#c9c9c9);display:flex;align-items:center;justify-content:center;box-shadow:0 3px 6px rgba(0,0,0,.2)}
.feature .orb-inner{width:166px;height:166px;border-radius:50%;display:flex;align-items:center;justify-content:center}
.orb-green{background:radial-gradient(circle at 50% 30%,#a4e046,#5fa514 70%,#4a8a0c)}
.orb-red{background:radial-gradient(circle at 50% 30%,#ff8a55,#ee4d1c 70%,#c9380c)}
.orb-yellow{background:radial-gradient(circle at 50% 30%,#ffee66,#f7cc1a 70%,#dca70a)}
.feature h3{margin-top:34px;font-size:17px;font-weight:700;color:var(--orange)}
.feature p{margin:6px auto 0;width:300px;font-size:12px;line-height:17px;color:#9a9a9a}

/* bands */
.band{left:0;width:1200px}
.band-how{top:992px;height:423px;background:radial-gradient(circle at 75% 50%,#ffa53a,var(--orange-band) 60%,#f07d06)}
.band-play{top:1415px;height:421px;background:var(--grey-bg)}
.band-earn{top:1836px;height:384px;background:radial-gradient(circle at 70% 40%,var(--purple-light),var(--purple) 70%)}
.band-title{font-family:"Montserrat",sans-serif;font-weight:700;font-size:54px;line-height:60px}
.band-text{width:440px;font-size:17px;line-height:23px}
.btn-more{width:125px;height:39px;background:linear-gradient(var(--orange-light),var(--orange));border:1px solid #e58a10;border-radius:3px;color:#fff;font-size:14px;font-weight:700;text-align:center;line-height:37px}
.light{color:#fff}
.light-text{color:#ffe9cf}
.photo{background:linear-gradient(135deg,rgba(255,255,255,.15),rgba(0,0,0,.1))}

/* footer */
.site-footer{left:0;top:2220px;width:1200px;height:377px;background:#f2f2f2}
.footer-card{left:117px;top:2246px;width:994px;height:307px;background:#fff;box-shadow:0 1px 4px rgba(0,0,0,.1)}
.footer-col h4{font-size:11px;font-weight:700;color:var(--teal);text-transform:uppercase}
.footer-col p{font-size:11px;line-height:19px;color:#999}
.copyright{font-size:11px;color:#999}
.copyright b{color:var(--teal)}
.follow{font-size:11px;color:#999;display:flex;align-items:center;gap:8px}
.follow .sq{width:12px;height:12px;background:var(--teal-mid);display:inline-block;border-radius:2px}
.follow .link{color:var(--teal);margin-right:22px;display:flex;align-items:center;gap:6px}
</style>
</head>
<body>

<header class="abs site-header">
  <div class="abs logo">LOGO</div>
  <div class="abs btn-signup">Sign Up</div>
  <div class="abs btn-login">Login</div>
</header>

<section>
  <div class="abs hero-photo" role="img" aria-label="Bright, softly blurred living room background"></div>
  <div class="abs hero-device" role="img" aria-label="Hands holding a tablet that shows a rewards store"></div>
  <h1 class="abs hero-title">Earn money doing what you love, playing games!</h1>
  <form class="abs signup-card">
    <h2>Start earning free gift cards today</h2>
    <div class="btn-social">Connect FriendNet</div>
    <div class="signup-note">or sign up with your email below</div>
    <div class="field" style="top:135px"><div class="ico"><svg width="14" height="10"><rect x="0.5" y="0.5" width="13" height="9" fill="none" stroke="#aaa"/><path d="M1 1l6 5 6-5" fill="none" stroke="#aaa"/></svg></div><span class="ph">Email</span></div>
    <div class="field" style="top:179px"><div class="ico"><svg width="12" height="14"><rect x="1" y="6" width="10" height="7" fill="#aaa"/><path d="M3 6V4a3 3 0 0 1 6 0v2" fill="none" stroke="#aaa" stroke-width="1.5"/></svg></div><span class="ph">Password</span></div>
    <div class="field" style="top:226px"><div class="ico"><svg width="12" height="14"><rect x="1" y="6" width="10" height="7" fill="#aaa"/><path d="M3 6V4a3 3 0 0 1 6 0v2" fill="none" stroke="#aaa" stroke-width="1.5"/></svg></div><span class="ph">Confirm Password</span></div>
    <div class="btn-start">Start now!</div>
  </form>
</section>

<section class="abs features">
  <div class="abs feature" style="left:20px;top:44px">
    <div class="orb"><div class="orb-inner orb-green">
      <svg width="80" height="50" viewBox="0 0 80 50"><path d="M18 6h44c10 0 16 10 16 24 0 12-8 16-14 10l-8-8H24l-8 8C10 46 2 42 2 30 2 16 8 6 18 6z" fill="#4d8e10"/><rect x="16" y="18" width="14" height="4" fill="#a4e046"/><rect x="21" y="13" width="4" height="14" fill="#a4e046"/><circle cx="56" cy="16" r="3" fill="#a4e046"/><circle cx="62" cy="22" r="3" fill="#a4e046"/></svg>
    </div></div>
    <h3>Play and share games</h3>
    <p>Etiam nisl erat, sollicitudin in laoreet ac, porta a justo. Vivamus metus justo, venenatis tincidunt porttitor sit amet, vehicula a massa.</p>
  </div>
  <div class="abs feature" style="left:420px;top:44px">
    <div class="orb"><div class="orb-inner orb-red">
      <svg width="64" height="52" viewBox="0 0 64 52"><path d="M4 12l14 14 14-22 14 22 14-14-6 30H10z" fill="#b5320a"/><rect x="10" y="44" width="44" height="6" fill="#b5320a"/></svg>
    </div></div>
    <h3>Get Rewards</h3>
    <p>Etiam nisl erat, sollicitudin in laoreet ac, porta a justo. Vivamus metus justo, venenatis tincidunt porttitor sit amet, vehicula a massa.</p>
  </div>
  <div class="abs feature" style="left:822px;top:44px">
    <div class="orb"><div class="orb-inner orb-yellow">
      <svg width="70" height="56" viewBox="0 0 70 56"><ellipse cx="34" cy="28" rx="26" ry="20" fill="#d19e08"/><rect x="18" y="42" width="8" height="12" fill="#d19e08"/><rect x="42" y="42" width="8" height="12" fill="#d19e08"/><rect x="60" y="24" width="8" height="8" fill="#d19e08"/><rect x="28" y="12" width="12" height="3" fill="#f7cc1a"/></svg>
    </div></div>
    <h3>Receive points</h3>
    <p>Etiam nisl erat, sollicitudin in laoreet ac, porta a justo. Vivamus metus justo, venenatis tincidunt porttitor sit amet, vehicula a massa.</p>
  </div>
</section>

<section class="abs band band-how">
  <div class="abs photo" style="left:610px;top:0;width:590px;height:423px" role="img" aria-label="Young woman using a tablet with floating game icons"></div>
  <h2 class="abs band-title light" style="left:114px;top:102px">How it works?</h2>
  <p class="abs band-text light-text" style="left:114px;top:172px">In dapibus arcu ac arcu rhoncus, ac eleifend eros lacinia. Maecenas tristique posuere lectus, at hendrerit dolor varius sed dolor varius sed..</p>
  <div class="abs btn-more" style="left:114px;top:254px">Know More</div>
</section>

<section class="abs band band-play">
  <div class="abs" style="left:78px;top:60px;width:467px;height:361px;background:linear-gradient(160deg,#e9c2a4,#d4a383 60%,#efefef)" role="img" aria-label="Hands holding a smartphone playing a game"></div>
  <h2 class="abs band-title" style="left:612px;top:116px;color:var(--teal)">Play games</h2>
  <p class="abs band-text" style="left:612px;top:186px;color:#a5a5a5">In dapibus arcu ac arcu rhoncus, ac eleifend eros lacinia. Maecenas tristique posuere lectus, at hendrerit dolor varius sed dolor varius sed..</p>
  <div class="abs btn-more" style="left:614px;top:260px">Know More</div>
</section>

<section class="abs band band-earn">
  <div class="abs photo" style="left:545px;top:0;width:655px;height:384px" role="img" aria-label="Excited man cheering while holding a tablet"></div>
  <h2 class="abs band-title light" style="left:114px;top:68px">Earn Money!</h2>
  <p class="abs band-text" style="left:114px;top:138px;color:#e3defa">In dapibus arcu ac arcu rhoncus, ac eleifend eros lacinia. Maecenas tristique posuere lectus, at hendrerit dolor varius sed dolor varius sed..</p>
  <div class="abs btn-more" style="left:114px;top:222px">Know More</div>
</section>

<footer class="abs site-footer"></footer>
<div class="abs footer-card">
  <svg class="abs" style="left:8px;top:56px" width="22" height="30" viewBox="0 0 22 30"><path d="M11 0a11 11 0 0 1 11 11c0 8-11 19-11 19S0 19 0 11A11 11 0 0 1 11 0z" fill="var(--teal)"/><circle cx="11" cy="11" r="4" fill="#fff"/></svg>
  <div class="abs footer-col" style="left:47px;top:55px">
    <h4>Contact us at:</h4>
    <p>Via Lorenza 12-18, City, 54000, Country<br>Phn: 1.900.555.014 &amp; Fax: 1.900.555.015<br>Email: <b style="color:var(--teal)">hello@lootpenny.org</b></p>
  </div>
  <div class="abs footer-col" style="left:327px;top:55px"><h4>About us:</h4><p>Dolor sit Ame<br>Adipiscing Porttitor<br>Euismod Arcu<br>Vitae Facilisis</p></div>
  <div class="abs footer-col" style="left:488px;top:55px"><h4>Services:</h4><p>Dolor sit Ame<br>Tincidunt<br>Adipiscing Porttitor<br>Euismod Arcu<br>Vitae Facilisis</p></div>
  <div class="abs footer-col" style="left:647px;top:55px"><h4>Case studies:</h4><p>Dolor sit Ame<br>Tincidunt<br>Adipiscing Porttitor<br>Euismod Arcu<br>Vitae Facilisis</p></div>
  <div class="abs footer-col" style="left:807px;top:55px"><h4>Careers:</h4><p>Euismod Arcu<br>Vitae Facilisis<br>Convallis Commodo</p></div>
  <div class="abs copyright" style="left:47px;top:226px">copyright 2013 - <b>Rule &amp; Ledger</b></div>
  <div class="abs follow" style="left:618px;top:224px">
    <span style="margin-right:14px">Follow us on:</span>
    <span class="link"><i class="sq"></i>FriendNet</span>
    <span class="link" style="color:#999"><i class="sq" style="background:#aaa"></i>Chirper</span>
    <span class="link" style="color:#999"><i class="sq" style="background:#aaa"></i>RSS</span>
  </div>
</div>

</body>
</html>
```